I am looking for a stand-out cover that sings out to new parents. The category is very pastel with limited compelling covers that would make me want to buy a book. This book will be used often in the first 12 months of baby's life - so must be strong enough to sit on the bedside table or on the coffee table to inspire reading. It will be a popular gift - so needs to look credible, "pick-up-able" and loveable.

The Book Title is - The Cradle Compass to Infancy's Opening Seasons: Grounded, Research-Led Methods on Rest, Nourishment, Protection plus Growing Assurance
The Size is - 8.5 x 11 in
Book description to be provided to final design for inclusion
Some examples of book covers in this category attached. Thanks

```html
<!DOCTYPE html>
<html lang="en">
<head>
<meta charset="utf-8">
<title>The Cradle Compass to Infancy's Opening Seasons – Cover</title>
<link rel="stylesheet" href="https://fonts.googleapis.com/css2?family=Varela+Round&family=Arimo:wght@400;700&display=swap">
<style>
  :root {
    --backdrop: #2b2b2b;
    --cover-cream: #ebe3c9;
    --ink: #1c1c1c;
    --title-red: #e0342b;
    --title-orange: #ec8526;
    --title-green: #2aae5b;
    --title-teal: #17a39b;
    --title-blue: #2a6db5;
    --title-navy: #28307d;
    --title-purple: #5b2f97;
    --band-gold: #a78a30;
    --band-text: #fbf6e6;
    --accent-sky: #2b96cc;
  }
  * { margin: 0; padding: 0; box-sizing: border-box; }
  html, body { width: 1200px; height: 800px; overflow: hidden; }
  body {
    background: var(--backdrop);
    display: flex;
    align-items: center;
    justify-content: center;
  }
  .book-cover {
    position: relative;
    width: 556px;
    height: 720px;
    background: var(--cover-cream);
    overflow: hidden;
  }
  .title-block {
    position: absolute;
    left: 0;
    right: 0;
    top: 150px;
    text-align: center;
    font-family: "Varela Round", sans-serif;
    text-transform: uppercase;
    line-height: 0.95;
  }
  .title-line { display: block; }
  .title-line--small {
    font-size: 46px;
    color: var(--title-red);
    letter-spacing: 2px;
    transform: rotate(-5deg) translateX(40px);
  }
  .title-line--mid {
    font-size: 96px;
    color: var(--title-orange);
    transform: rotate(-4deg) translateX(30px);
  }
  .title-line--large {
    font-size: 92px;
    background: linear-gradient(90deg, var(--title-green), var(--title-teal) 45%, var(--title-blue) 70%, var(--title-purple));
    -webkit-background-clip: text;
    background-clip: text;
    color: transparent;
    transform: rotate(-3deg);
  }
  .subtitle-band {
    position: absolute;
    left: 96px;
    top: 448px;
    padding: 8px 18px;
    background: var(--band-gold);
    color: var(--band-text);
    font-family: "Arimo", sans-serif;
    font-size: 19px;
    letter-spacing: 0.5px;
    text-transform: uppercase;
    transform: rotate(-3deg);
  }
  .subtitle-band strong { font-weight: 700; }
  .tagline {
    position: absolute;
    left: 56px;
    right: 56px;
    top: 530px;
    font-family: "Arimo", sans-serif;
    font-size: 18px;
    line-height: 1.4;
    color: var(--ink);
    text-align: center;
  }
  .ornament {
    position: absolute;
    border-radius: 10px;
    opacity: 0.35;
  }
  .ornament--confetti-left {
    left: 44px; top: 230px; width: 70px; height: 60px;
    background: radial-gradient(circle, #e0559a, transparent 70%);
  }
  .ornament--confetti-right {
    right: 40px; top: 128px; width: 80px; height: 60px;
    background: radial-gradient(circle, var(--accent-sky), transparent 70%);
  }
  .ornament--vane {
    right: 36px; top: 380px; width: 90px; height: 50px;
    background: radial-gradient(circle, #3a3a3a, transparent 70%);
  }
  .ornament--leaf {
    right: 90px; top: 470px; width: 40px; height: 40px;
    background: radial-gradient(circle, #c8643a, transparent 70%);
  }
</style>
</head>
<body>
  <main class="book-cover">
    <div class="ornament ornament--confetti-left" role="img" aria-label="Scattered confetti, stars and a small ribbon bow"></div>
    <div class="ornament ornament--confetti-right" role="img" aria-label="Colourful stars and confetti beside a small cloud"></div>
    <div class="ornament ornament--vane" role="img" aria-label="Small weather vane with a rooster and arrow"></div>
    <div class="ornament ornament--leaf" role="img" aria-label="Small autumn leaf"></div>

    <h1 class="title-block">
      <span class="title-line title-line--small">The</span>
      <span class="title-line title-line--mid">Cradle</span>
      <span class="title-line title-line--large">Compass</span>
    </h1>

    <p class="subtitle-band">To Infancy's <strong>Opening Seasons</strong></p>

    <p class="tagline">Grounded, Research-Led Methods on<br>Rest, Nourishment, Protection plus Growing Assurance</p>
  </main>
</body>
</html>
```